Criação de Folder para Consultoria de Negócios
" Possuímos 30 PAs com assistentes de pré-vendas que prospectam leads para os nossos clientes via telefone e e-mail. "

```html
<!DOCTYPE html>
<html lang="pt-BR">
<head>
<meta charset="utf-8">
<title>Folder – Consultoria de Negócios</title>
<link href="https://fonts.googleapis.com/css2?family=Montserrat:wght@500;700;800&family=Open+Sans:wght@400;600;700&display=swap" rel="stylesheet">
<style>
:root{
  --orange:#f07d1a;
  --orange-dark:#d9650a;
  --ink:#1f1f1f;
  --text:#4a4a4a;
  --muted:#8a8a8a;
  --paper:#ffffff;
  --stage:#e9e6e1;
  --dark:#262626;
}
*{margin:0;padding:0;box-sizing:border-box}
html,body{width:1200px;height:1200px;overflow:hidden;background:var(--stage)}
body{font-family:"Open Sans",Arial,sans-serif;color:var(--text)}
.brochure{position:absolute;left:30px;top:310px;width:1140px;height:580px;display:flex;background:var(--paper);box-shadow:0 10px 30px rgba(0,0,0,.15)}
.panel{position:relative;width:380px;height:100%;overflow:hidden;border-right:1px solid #eee}
.panel:last-child{border-right:none}
.bottom-strip{position:absolute;left:0;bottom:0;width:100%;height:10px;background:var(--orange)}
.tab{display:inline-block;background:var(--orange);color:#fff;font-family:"Montserrat",sans-serif;font-weight:700;font-size:13px;padding:6px 26px;border-radius:0 0 6px 6px}
h2{font-family:"Montserrat",sans-serif;font-weight:800;color:var(--ink);font-size:15px}
h3{font-family:"Montserrat",sans-serif;font-weight:700;color:var(--orange);font-size:11.5px;margin-bottom:3px}
p{font-size:9.5px;line-height:1.5}

/* left panel */
.services{text-align:center}
.service-row{display:flex;justify-content:space-around;padding:16px 14px 8px}
.service{width:62px;text-align:center}
.service .dot{width:40px;height:40px;border-radius:50%;background:var(--dark);margin:0 auto 6px;display:flex;align-items:center;justify-content:center}
.service span{font-size:7.5px;line-height:1.3;display:block;color:var(--text)}
.values{padding:6px 30px 0;text-align:center}
.values h2{font-size:13px;margin:8px 0 3px}
.results{position:absolute;left:0;top:318px;width:100%;height:252px;background:var(--dark);display:flex}
.chart{width:170px;padding:18px 12px}
.chart h3{color:#fff;font-size:10px}
.list{flex:1;background:var(--orange);margin:18px 14px 18px 0;padding:10px}
.list li{list-style:none;background:#fff;color:var(--ink);font-size:9.5px;font-weight:600;padding:6px 8px;margin-bottom:6px;display:flex;gap:8px}
.list li b{color:var(--orange);font-family:"Montserrat",sans-serif;min-width:34px}

/* middle panel */
.photo{width:100%;display:block}
.method{padding:0 26px}
.method .tab{margin:-14px 0 10px;border-radius:6px;position:relative}
.method h2{margin-bottom:4px}
.method .sub{font-size:9.5px;color:var(--muted);margin-bottom:12px}
.method section{margin-bottom:10px}
.quote{border-left:3px solid var(--orange);padding-left:8px;font-style:italic;color:var(--ink)}

/* right panel */
.about{padding:20px 26px 0}
.about section{margin-bottom:10px}
.contact{position:absolute;left:0;top:290px;width:100%;height:280px}
.contact-text{position:absolute;left:0;top:40px;width:100%;text-align:center;padding:0 20px}
.contact-text .lead{font-family:"Montserrat",sans-serif;font-weight:700;color:var(--orange);font-size:14px}
.contact-text .url{font-family:"Montserrat",sans-serif;font-weight:800;color:var(--ink);font-size:13px;margin:4px 0 12px}
.contact-text .note{color:var(--orange);font-weight:700;font-size:12px;line-height:1.35}
.phone{display:flex;align-items:center;justify-content:center;gap:8px;margin-top:14px;font-family:"Montserrat",sans-serif;font-weight:800;color:var(--orange);font-size:22px}
</style>
</head>
<body>
<main class="brochure">

  <!-- Panel 1 -->
  <section class="panel services">
    <div class="tab">Nossos Serviços</div>
    <div class="service-row">
      <div class="service"><div class="dot"><svg width="20" height="20" viewBox="0 0 20 20"><rect x="3" y="6" width="14" height="10" rx="1" fill="none" stroke="#f07d1a" stroke-width="2"/><rect x="7" y="3" width="6" height="3" fill="#f07d1a"/></svg></div><span>Consultoria comercial</span></div>
      <div class="service"><div class="dot"><svg width="20" height="20" viewBox="0 0 20 20"><path d="M5 3h4l1 4-2 1a9 9 0 0 0 4 4l1-2 4 1v4a2 2 0 0 1-2 2A14 14 0 0 1 3 5a2 2 0 0 1 2-2z" fill="#f07d1a"/></svg></div><span>Prospecção por telefone</span></div>
      <div class="service"><div class="dot"><svg width="20" height="20" viewBox="0 0 20 20"><rect x="3" y="5" width="14" height="10" fill="none" stroke="#f07d1a" stroke-width="2"/><path d="M3 5l7 6 7-6" fill="none" stroke="#f07d1a" stroke-width="2"/></svg></div><span>Contato por e-mail</span></div>
      <div class="service"><div class="dot"><svg width="20" height="20" viewBox="0 0 20 20"><circle cx="10" cy="10" r="7" fill="none" stroke="#f07d1a" stroke-width="2"/><circle cx="10" cy="10" r="3" fill="#f07d1a"/></svg></div><span>Geração de leads</span></div>
      <div class="service"><div class="dot"><svg width="20" height="20" viewBox="0 0 20 20"><path d="M4 16V9M9 16V5M14 16v-4" stroke="#f07d1a" stroke-width="3"/></svg></div><span>Relatórios de resultado</span></div>
    </div>
    <div class="values">
      <h2>Nossa Missão</h2>
      <p>Gerar oportunidades reais de negócio para nossos clientes, com um time dedicado de pré-vendas.</p>
      <h2>Nossa Visão</h2>
      <p>Ser referência nacional em prospecção ativa e aceleração de vendas B2B até o próximo ano.</p>
    </div>
    <div class="results">
      <div class="chart">
        <h3>Crescimento</h3>
        <svg width="146" height="170" viewBox="0 0 146 170">
          <line x1="0" y1="165" x2="146" y2="165" stroke="#666"/>
          <rect x="6" y="125" width="18" height="40" fill="#f07d1a"/>
          <rect x="34" y="100" width="18" height="65" fill="#f07d1a"/>
          <rect x="62" y="80" width="18" height="85" fill="#f07d1a"/>
          <rect x="90" y="50" width="18" height="115" fill="#f07d1a"/>
          <rect x="118" y="20" width="18" height="145" fill="#f07d1a"/>
        </svg>
      </div>
      <ul class="list">
        <li><b>30</b>PAs de pré-vendas</li>
        <li><b>12</b>Segmentos atendidos</li>
        <li><b>+5 mil</b>Leads gerados</li>
        <li><b>98%</b>Clientes satisfeitos</li>
        <li><b>24h</b>Início da operação</li>
      </ul>
    </div>
    <div class="bottom-strip"></div>
  </section>

  <!-- Panel 2 -->
  <section class="panel">
    <svg class="photo" width="380" height="170" role="img" aria-label="Fotografia de mãos unindo peças de quebra-cabeça sobre a mesa">
      <defs><linearGradient id="g1" x1="0" y1="0" x2="1" y2="1"><stop offset="0" stop-color="#d8d3cf"/><stop offset=".6" stop-color="#c9a58a"/><stop offset="1" stop-color="#5a5a5a"/></linearGradient></defs>
      <rect width="380" height="170" fill="url(#g1)"/>
    </svg>
    <div class="method">
      <div class="tab">Como trabalhamos</div>
      <h2>Método Impulso Comercial (MIC)</h2>
      <div class="sub">Processo estruturado para acelerar suas vendas</div>
      <section><h3>Diagnóstico Comercial</h3><p>Analisamos seu mercado, público e funil para definir o perfil ideal de cliente e a abordagem certa.</p></section>
      <section><h3>Plano de Ação</h3><p>Criamos roteiros, listas e metas semanais alinhadas ao seu time de vendas e aos seus objetivos.</p></section>
      <section><h3>Pré-vendas Ativa</h3><p class="quote">"Possuímos 30 PAs com assistentes de pré-vendas que prospectam leads para os nossos clientes via telefone e e-mail."</p></section>
      <section><h3>Acompanhamento</h3><p>Relatórios claros e reuniões periódicas para medir e melhorar cada resultado.</p></section>
    </div>
    <div class="bottom-strip"></div>
  </section>

  <!-- Panel 3 -->
  <section class="panel">
    <div class="about">
      <section><h3>Quem somos</h3><p>Somos uma consultoria de negócios focada em gerar demanda qualificada para empresas que querem vender mais.</p></section>
      <section><h3>Nosso time</h3><p>Profissionais treinados em abordagem consultiva, prontos para representar sua marca com qualidade.</p></section>
      <section><h3>Por que nós</h3><p>Agilidade na implantação, custo previsível e foco total em reuniões agendadas para o seu time.</p></section>
    </div>
    <div class="contact">
      <svg width="380" height="280" role="img" aria-label="Fotografia de escritório com equipe em reunião, esmaecida">
        <defs><linearGradient id="g2" x1="0" y1="0" x2="0" y2="1"><stop offset="0" stop-color="#ffffff"/><stop offset=".35" stop-color="#e6e8ea"/><stop offset="1" stop-color="#a9b0b6"/></linearGradient></defs>
        <rect width="380" height="280" fill="url(#g2)"/>
      </svg>
      <div class="contact-text">
        <div class="lead">Acesse nosso site</div>
        <div class="url">www.vendaplenaconsultoria.com.br</div>
        <div class="note">E saiba mais sobre<br>nossos serviços<br>ou agende uma reunião</div>
        <div class="phone">
          <svg width="22" height="22" viewBox="0 0 20 20"><circle cx="10" cy="10" r="10" fill="#f07d1a"/><path d="M7 5h2l1 2.5-1.3.8a6 6 0 0 0 3 3l.8-1.3L15 11v2a1.5 1.5 0 0 1-1.5 1.5A8.5 8.5 0 0 1 5.5 6.5 1.5 1.5 0 0 1 7 5z" fill="#fff"/></svg>
          (11) 4000-2718
        </div>
      </div>
    </div>
    <div class="bottom-strip"></div>
  </section>

</main>
</body>
</html>
```